Briefpapier und Visitenkarten
Zielgruppe
Das Design soll Herren im mittleren bis hohen Alter ansprechen.
Aufgabenstellung
Benötigt wird ein Briefpapier für die Koresspondenz und die Rechnungen. Ein Logo ist vorhanden und muss ins Briefpapier und auf die Visitenkarten einbebunden werden.

```html
<!DOCTYPE html>
<html lang="de">
<head>
<meta charset="utf-8">
<title>helvanet systems – Visitenkarte</title>
<link href="https://fonts.googleapis.com/css2?family=Arimo:wght@400;700&display=swap" rel="stylesheet">
<style>
  :root {
    --backdrop: #9b9b9b;
    --card: #ffffff;
    --brand-red: #c0112b;
    --ink: #111111;
  }
  * { margin: 0; padding: 0; box-sizing: border-box; }
  html, body {
    width: 864px;
    height: 1200px;
    overflow: hidden;
    background: var(--backdrop);
    font-family: "Arimo", Arial, sans-serif;
    color: var(--ink);
  }
  .sheet { position: relative; width: 864px; height: 1200px; }
  .card {
    position: absolute;
    left: 104px;
    width: 648px;
    height: 418px;
    background: var(--card);
    border-radius: 26px;
    overflow: hidden;
  }
  .card--front { top: 145px; }
  .card--back { top: 610px; }

  .wordmark {
    position: absolute;
    left: 0; right: 0;
    top: 184px;
    display: flex;
    align-items: center;
    justify-content: center;
    gap: 16px;
  }
  .wordmark__dot {
    width: 40px; height: 40px;
    border-radius: 50%;
    background: var(--brand-red);
  }
  .wordmark__name {
    font-size: 48px;
    font-weight: 400;
    color: var(--brand-red);
    letter-spacing: 0.5px;
    line-height: 1;
  }

  .contact {
    position: absolute;
    left: 46px;
    top: 76px;
    font-size: 19px;
    line-height: 26.5px;
  }
  .contact__person { font-weight: 700; }
  .contact__address { margin-top: 15px; }
  .contact__phones { margin-top: 17px; font-weight: 700; }
  .contact__phones dt { float: left; width: 82px; clear: left; }
  .contact__phones dd { margin-left: 82px; }

  .corner-disc {
    position: absolute;
    right: -150px;
    bottom: -150px;
    width: 300px;
    height: 300px;
    border-radius: 50%;
    background: var(--brand-red);
  }
</style>
</head>
<body>
<main class="sheet">
  <section class="card card--front" aria-label="Vorderseite">
    <div class="wordmark">
      <span class="wordmark__dot" aria-hidden="true"></span>
      <span class="wordmark__name">helvanet systems</span>
    </div>
  </section>

  <section class="card card--back" aria-label="Rückseite">
    <div class="contact">
      <p class="contact__person">Jonas Beispiel<br>Supertolle Jobposition</p>
      <p class="contact__address">
        Lindenweg 12<br>
        49780 Beispielstadt<br>
        jbeispiel@helvanet.com<br>
        www.helvanet.de
      </p>
      <dl class="contact__phones">
        <dt>Tel.:</dt><dd>0 58 21 / 37 90</dd>
        <dt>Mobil:</dt><dd>0171 / 46 02 19 58</dd>
      </dl>
    </div>
    <span class="corner-disc" aria-hidden="true"></span>
  </section>
</main>
</body>
</html>
```